Recruitment Package Design for Healthcare Organization

We need a brochure designed that matches the design of our website and logo. The focus of the brochure is to provide information about our organization and region to prospective physicians looking to join our team. I have the content already put together, but would like some imagery of local geography/activities to be incorporated into the design. I have attached the content document as well as an example we are wanting to model ours after.

Our website is: https://brightmarrowcare.ca/

Target Market(s)

Prospective physicians

Industry/Entity Type

Healthcare

Requirements
Must have
• Local imagery which I have attached.

```html
<!DOCTYPE html>
<html lang="en">
<head>
<meta charset="utf-8">
<title>Brightmarrow Care – Physician Recruitment Package</title>
<link href="https://fonts.googleapis.com/css2?family=Montserrat:wght@500;600&family=Open+Sans:ital,wght@0,400;0,700;1,400&display=swap" rel="stylesheet">
<style>
:root{
  --stage:#7b7b7b;
  --paper:#ffffff;
  --tint:#f1fbfc;
  --cyan:#2fd0db;
  --cyan-dark:#1fb8c4;
  --heading-box:#8c8c8c;
  --ink:#555a5e;
  --ring:#8e8e8e;
}
*{box-sizing:border-box;margin:0;padding:0}
html,body{width:1200px;height:4968px;overflow:hidden}
body{background:var(--stage);position:relative;font-family:"Open Sans",Arial,sans-serif;color:var(--ink)}
.page{position:absolute;left:397px;width:409px;height:575px;background:var(--paper);overflow:hidden}
.page--inner{padding:24px 18px 18px 26px}
.page--tinted{background:var(--tint)}
.page--inner::before{content:"";position:absolute;left:12px;top:10px;bottom:10px;width:1.5px;background:var(--cyan)}
.page-number{position:absolute;right:22px;top:18px;font-family:"Montserrat",sans-serif;font-size:22px;font-weight:500;color:var(--heading-box)}
.section-title{display:table;margin:0 auto 10px;background:var(--heading-box);color:#fff;font-family:"Montserrat",sans-serif;font-weight:600;font-size:13px;padding:5px 14px;border-bottom:2px solid #6f6f6f}
.section-title--left{margin-left:0}
p{font-size:5.6px;line-height:1.35;margin-bottom:6px}
p strong{color:#444}
.link{color:var(--cyan-dark)}
.subtitle{text-align:center;color:var(--cyan-dark);font-size:5.8px;margin-bottom:8px}
.callout{background:var(--cyan);color:#fff;border-radius:8px;padding:9px 12px;margin:6px 0 10px;font-weight:700}
.callout p{color:#fff;margin-bottom:5px}
.callout--media{display:flex;align-items:center;gap:10px}
.callout--media p{flex:1}
.photo{flex:none;border-radius:50%;border:2px solid #fff}
.quote{font-style:italic;color:#6a6f73}
.divider{width:80px;height:1px;background:var(--cyan);margin:7px auto}
.bubbles{position:relative;width:90px;height:70px;flex:none}
.bubbles span{position:absolute;border-radius:50%;background:#fff}
.cover-brand{position:absolute;left:95px;top:40px;display:flex;align-items:center;gap:10px}
.cover-brand__dot{width:30px;height:30px;border-radius:50%;background:var(--cyan)}
.cover-brand__name{font-family:"Open Sans",sans-serif;font-weight:400;color:var(--cyan);font-size:26px;line-height:1}
.cover-art{position:absolute;left:0;top:0}
.todo-grid{display:grid;grid-template-columns:1fr 1fr;column-gap:24px;row-gap:6px;padding:0 6px}
.todo-group{border-left:1px solid var(--cyan);padding-left:6px}
.todo-group h3{font-size:6.4px;color:var(--cyan-dark);font-weight:700;margin-bottom:4px}
.todo-group li{list-style:none;font-size:5px;line-height:1.35}
.todo-photo-row{grid-column:1 / 3;display:flex;justify-content:space-around;padding:4px 0}
.todo-photo-row--center{justify-content:center}
.info-block{text-align:center;margin-top:22px}
.info-block h3{font-size:6.4px;font-weight:400;color:var(--cyan-dark);margin-bottom:10px}
.info-block li{list-style:none;font-size:5.4px;line-height:1.9}
</style>
</head>
<body>

<section class="page page--cover" style="top:226px">
  <svg class="cover-art" width="409" height="575" viewBox="0 0 409 575" aria-hidden="true">
    <circle cx="360" cy="470" r="250" fill="var(--cyan)"/>
    <path d="M65 520 A300 300 0 0 1 400 220" fill="none" stroke="var(--ring)" stroke-width="4"/>
  </svg>
  <div class="cover-brand">
    <span class="cover-brand__dot"></span>
    <span class="cover-brand__name">brightmarrow care</span>
  </div>
</section>

<section class="page page--inner" style="top:888px">
  <span class="page-number">1</span>
  <h2 class="section-title">CEO Message</h2>
  <p><strong>Thank you for your interest in Brightmarrow Care</strong> – whether you are a recent graduate looking to establish your practice or a veteran physician looking for a change, I am confident you can find your healthcare home here. It is my privilege to lead an organization that is truly committed to creating the best possible experiences and outcomes for our patients and the communities we serve. As the Okanagan's population has boomed over the last decade, there is even greater need to provide residents with access to essential healthcare services. Our time-tested and scalable operating model has enabled us to not only survive, but thrive through the many challenges that the past 5 years have presented the healthcare industry.</p>
  <p>Founded in 2016, Brightmarrow Care is an established organization with a strong reputation in the communities we serve. From a business perspective, our revenue is healthy and our trajectory is positive. The numbers back this up:</p>
  <div class="callout">
    <p>In fiscal year 2024, Brightmarrow Care provided more than 160,000 patient visits.</p>
    <p>Fiscal year 2024 gross annual revenue was $3.49 million, representing a 70% year-over-year growth rate from fiscal year 2023.</p>
    <p>Year-to-date gross revenue is up 3.4% over the same period last year.</p>
  </div>
  <p>Brightmarrow Care is led by an experienced and well-balanced leadership team which includes our medical directors, management team and senior leadership team. This unique combination of backgrounds and experiences helps to inform and shape the decisions and direction of the organization. If you would like to learn more about how we continue to keep our commitment of "creating exceptional experiences for every patient, every time," I encourage you to visit our website at <span class="link">www.brightmarrowcare.ca</span>.</p>
  <p>Sincerely,<br>Dorian Hale, CEO</p>
  <h2 class="section-title" style="margin-top:12px">About Dorian and Maren Hale</h2>
  <p>Prior to working in the healthcare industry, Dorian spent 15 years in operations and human resources management for a large communications company. After shifting focus to the healthcare industry 9 years ago, he took on the role of Operations Manager for a pharmacy chain and was tasked with getting our first two locations built, staffed and operational. These clinics, Ridgeview Medical Clinic and Loon Point Medical Clinic, pre-dated the Brightmarrow Care name, but were the foundation upon which it was built. In 2020, along with his wife Maren, a registered nurse and soon-to-be business partner, they purchased the two clinics and Brightmarrow Care was born. Since then, Dorian and Maren's combination of experience in healthcare, human resources and operations management has enabled them to grow the organization to 4 locations with 50+ providers across 6 specialties. Dorian and Maren's passion and dedication to improving the lives of others, whether it be our patients, employees or physicians, is evident in every aspect of our organization and is articulated via our mission statement and core values.</p>
</section>

<section class="page page--inner" style="top:1550px">
  <span class="page-number">2</span>
  <h2 class="section-title">Our Mission</h2>
  <p><strong>Creating exceptional patient experiences for every patient, every time</strong> is not just our mission statement – it's a commitment to our patients. By creating a culture where we value the quality of care every patient receives first and foremost, that empowers our employees and providers to grow, and that treats every patient with compassion, dignity and respect, we deliver on our promise to our patients.</p>
  <h2 class="section-title" style="margin-top:10px">Our History</h2>
  <p><strong>Our quest to deliver consistent access to care and to provide physicians with a healthy work/life balance</strong> began 9 years ago and is still the driving force behind our mission today. Brightmarrow Care started when a local pharmacist saw an opportunity to help his community that was struggling with a severe physician shortage and where thousands of people could not access care when or where they needed it. By offering physicians an operating model that gave them the ability to practice medicine without the stress of having to manage a business, a low overhead and the flexibility to practice medicine on their terms, and with the help of an experienced operations manager, he was immediately successful in attracting new physicians to the area when many others had failed. This idea became a reality when we opened our first location, Loon Point Medical Clinic, in Lake Country, BC in 2016. A year later, our second location, Ridgeview Medical Clinic opened with the same vision and the same result.</p>
  <div class="callout callout--media">
    <p>In May of 2020, during the height of the pandemic, our then operations manager, Dorian Hale, approached the owner of the clinics about selling the company to him and his wife Maren. They saw an opportunity to help thousands more people secure access to care and to help physicians find a solution to the administrative burnout that was causing so many to leave family medicine at the time. Brightmarrow Care was born.</p>
    <div class="bubbles" aria-hidden="true">
      <span style="width:56px;height:56px;right:4px;top:0"></span>
      <span style="width:40px;height:40px;left:0;bottom:0"></span>
    </div>
  </div>
  <p>In 2021, we opened our third location in the Pandosy neighbourhood of Kelowna, the first location bearing the Brightmarrow Care name and also our first foray into multidisciplinary care with Sports Medicine and Family Practice providers working together in the same building. Later that same year, the Keystone Medical team joined Brightmarrow and became our central Kelowna location, Brightmarrow Care – Springfield. After nearly a year of extensive renovations, the maternity care and family medicine group from Alder Run Family Medicine relocated and joined us at our Springfield location in early 2023.</p>
  <p>Today Brightmarrow Care is comprised of more than 50 providers across 6 specialties and 4 locations. We are the largest, privately owned provider of primary care services in the Okanagan region and provide care to more than 60,000 residents.</p>
</section>

<section class="page page--inner page--tinted" style="top:2212px">
  <span class="page-number">3</span>
  <h2 class="section-title">Testimonials</h2>
  <p><strong>We believe that our employees are our greatest asset</strong>, and we strive to treat them with the same level of compassion, dignity, and respect that we provide to our patients. Employees' voices often speak the loudest about an organization's culture. To that end, we've highlighted genuine comments submitted by Brightmarrow Care employees and providers that reflect our Mission, Values and commitment to them.</p>
  <div class="divider"></div>
  <p class="quote">I am a physician who has worked the past 47 years in Canada and the USA. One of my best experiences was to practice in Lake Country, BC at Brightmarrow Care. Their onboarding team made our 4 years back in Canada a wonderful experience and their model allowed me to work as hard as I wanted, but also to take time off as desired. The overhead was reasonable and the work environment was great.</p>
  <div class="divider"></div>
  <p class="quote">The leadership of Brightmarrow were open to suggestions and made the transition into their office a pleasure. Lake Country! Kelowna is one of the best areas in Canada, with plenty of leisure activities year round. The only reason we returned to the US was my wife's desire to be back close to our children and grandchildren. If it was my choice I would still be there.</p>
  <div class="divider"></div>
  <p class="quote">During covid, Brightmarrow transitioned to virtual medicine and then later to a hybrid model which I am sure will make my practice more adaptable. The reimbursement in BC is a great opportunity to adapt work to life balance and still get paid well. There is no better partner to work with in the Okanagan than Brightmarrow Care!</p>
  <div class="divider"></div>
  <p class="quote">I've had the pleasure of working with the team at Brightmarrow Care since 2018 as a part-time physician. During this time, I've served both as a family doctor and locum physician, primarily at the Loon Point Medical Clinic in Lake Country, BC.</p>
  <p class="quote">Having previously co-owned three medical clinics in the Central Okanagan, I truly appreciate how Brightmarrow Care has removed the administrative burdens that come with clinical practice. This allows me to focus solely on what I was trained to do – providing patient care.</p>
  <div class="divider"></div>
  <p class="quote">Brightmarrow Care fosters a welcoming and supportive environment for physicians, tailoring opportunities to align with each doctor's unique work goals. Management is approachable, responsive, and genuinely open to suggestions from both physicians and staff, creating a culture where collaboration thrives.</p>
  <div class="divider"></div>
  <p class="quote">The clinic's record system is by far the most user-friendly I've encountered, further enhancing efficiency and workflow. I wholeheartedly recommend working with Brightmarrow Care. The supportive atmosphere, administrative relief, and innovative leadership make it my top choice for clinical practice – I wouldn't work anywhere else.</p>
</section>

<section class="page page--inner" style="top:2874px">
  <span class="page-number" style="top:12px">4</span>
  <h2 class="section-title section-title--left">About Kelowna and The Okanagan Valley</h2>
  <p class="subtitle">If you are considering working or living in the Kelowna area, take a look at all that the Okanagan Valley has to offer.</p>
  <p>Nestled in the heart of British Columbia, the Okanagan Valley offers a lifestyle like no other. Wake up to stunning lake views, hike through breathtaking mountain trails, and spend your days exploring world-class vineyards, sandy beaches, and outdoor adventures. Whether you're skiing in winter, boating in summer, or enjoying vibrant arts and local culture, the Okanagan Valley is a place to live life to the fullest. Come for the natural beauty, stay for the laid-back lifestyle!</p>
  <p>Kelowna has experienced a population growth of 14% since 2016, making it the fastest growing metropolitan area in Canada. With over 165,000 residents, and a median age of 42, it is also the 4th largest, and one of the youngest cities in the province of British Columbia.</p>
  <div class="callout callout--media">
    <p>Situated in the heart of the Okanagan Valley, Kelowna is surrounded by mountains, lakes and vineyards where residents embrace outdoor adventures and an active lifestyle all year long. The city is also an economic powerhouse, home to robust traditional sectors like agriculture and construction, and burgeoning new sectors such as information technology.</p>
    <svg class="photo" width="62" height="62" viewBox="0 0 62 62" role="img" aria-label="Photo of Kelowna waterfront and lake">
      <defs><linearGradient id="g1" x1="0" y1="0" x2="0" y2="1"><stop offset="0" stop-color="#a9c7dd"/><stop offset=".55" stop-color="#6d8aa1"/><stop offset="1" stop-color="#3d5462"/></linearGradient></defs>
      <circle cx="31" cy="31" r="31" fill="url(#g1)"/>
    </svg>
  </div>
  <h2 class="section-title">Healthcare</h2>
  <p class="subtitle">Climate and Outdoor Recreation</p>
  <p>The Okanagan Valley offers an abundance of outdoor activities ranging from water sports in the summer to skiing in the winter, as well as hiking, biking, and opportunities for recreation and nature immersion. It's a great place for year-round outdoor adventure, including 30 provincial parks, more than 100 lakes, same-day access to 5 world class ski resorts and 165 wineries.</p>
  <div class="callout callout--media">
    <p>With over 2,000 hours of sunshine a year, the Okanagan Valley boasts one of the best climates in Canada. Enjoy warm, dry summers ideal for outdoor activities, relaxing at lakeside beaches, and exploring vineyards. Winters bring a beautiful blanket of mild temperatures and snowy mountain peaks – famous for their light, dry powder. Whether you're a sun-seeker or snow-lover, the Okanagan offers the ideal climate year-round with average daytime high temperatures ranging from 1°C (33°F) in January to 28°C (82°F) in July.</p>
    <svg class="photo" width="62" height="62" viewBox="0 0 62 62" role="img" aria-label="Photo of the Okanagan Valley city skyline and hills">
      <defs><linearGradient id="g2" x1="0" y1="0" x2="0" y2="1"><stop offset="0" stop-color="#b9d4e6"/><stop offset=".5" stop-color="#7b9a7a"/><stop offset="1" stop-color="#4f6650"/></linearGradient></defs>
      <circle cx="31" cy="31" r="31" fill="url(#g2)"/>
    </svg>
  </div>
</section>

<section class="page page--inner page--tinted" style="top:3536px">
  <span class="page-number">5</span>
  <h2 class="section-title" style="margin-bottom:14px">Things to do</h2>
  <div class="todo-grid">
    <div class="todo-group">
      <h3>Attractions</h3>
      <ul><li>Lakeside Aerospace Centre</li><li>Valley Discovery Science Centre</li><li>Cedar Gorge Trestle Trail</li><li>Lakeshore Aquatic Centre</li><li>Wallaby Hollow Farm</li><li>Valley Greenway Trail</li><li>Okanagan Lake</li><li>Lakeview Events Arena</li></ul>
    </div>
    <div class="todo-group">
      <h3>Parks</h3>
      <ul><li>Birch Bend Park</li><li>Sandbar Waterfront Park</li><li>Shoreline Regional Park</li><li>Summit Lookout Park</li><li>Central City Park</li><li>Willow Creek Greenway</li><li>High Ridge Wilderness Park</li></ul>
    </div>
    <div class="todo-photo-row todo-photo-row--center">
      <svg class="photo" width="96" height="96" viewBox="0 0 96 96" role="img" aria-label="Photo of a snowy ski lift in winter">
        <defs><linearGradient id="g3" x1="0" y1="0" x2="0" y2="1"><stop offset="0" stop-color="#9fc8e6"/><stop offset=".6" stop-color="#d9e8f2"/><stop offset="1" stop-color="#ffffff"/></linearGradient></defs>
        <circle cx="48" cy="48" r="48" fill="url(#g3)"/>
      </svg>
    </div>
    <div class="todo-group">
      <h3>Arts</h3>
      <ul><li>Valley Symphony Orchestra</li><li>Lakeside Art House</li><li>Harbour Centre for the Arts</li><li>Footlight Dinner Theatre</li><li>Valley Heritage Museum</li><li>Orchard and Vine Museum</li></ul>
    </div>
    <div class="todo-group">
      <h3>Events</h3>
      <ul><li>Summer Lakefront Festival</li><li>Across the Lake Swim</li><li>Riverside Music Festival</li><li>Harvest Vine Festival</li><li>Ridge Road Hill Climb</li></ul>
    </div>
    <div class="todo-photo-row">
      <svg class="photo" width="84" height="84" viewBox="0 0 84 84" role="img" aria-label="Photo of a rock climber on red cliffs">
        <defs><linearGradient id="g4" x1="0" y1="0" x2="1" y2="1"><stop offset="0" stop-color="#cfe4f2"/><stop offset=".5" stop-color="#b0603a"/><stop offset="1" stop-color="#6e3722"/></linearGradient></defs>
        <circle cx="42" cy="42" r="42" fill="url(#g4)"/>
      </svg>
      <svg class="photo" width="84" height="84" viewBox="0 0 84 84" role="img" aria-label="Photo of lakeside vineyards">
        <defs><linearGradient id="g5" x1="0" y1="0" x2="0" y2="1"><stop offset="0" stop-color="#a8cbe2"/><stop offset=".5" stop-color="#7ea06a"/><stop offset="1" stop-color="#4c6b3c"/></linearGradient></defs>
        <circle cx="42" cy="42" r="42" fill="url(#g5)"/>
      </svg>
    </div>
    <div class="todo-group">
      <h3>Higher Education</h3>
      <ul><li>Lakeshore University – Okanagan</li><li>Valley Ridge College</li><li>Harbourline Design Institute</li><li>Interior Institute of Applied Trades</li></ul>
    </div>
    <div class="todo-group">
      <h3>Sports</h3>
      <ul><li>Lakeside Fireballs Junior Hockey Team</li><li>Lakeside Kestrels Baseball</li><li>Lakeside Sun Football</li><li>Lakeside Lancers Lacrosse</li></ul>
    </div>
  </div>
</section>

<section class="page page--inner" style="top:4198px">
  <span class="page-number">6</span>
  <h2 class="section-title">Additional Information</h2>
  <div class="info-block">
    <h3>Brightmarrow Care</h3>
    <ul><li>https://brightmarrowcare.ca/about-us/</li><li>https://brightmarrowcare.ca/clinics/</li><li>https://brightmarrowcare.ca/specialties/</li><li>https://brightmarrowcare.ca/careers/</li></ul>
  </div>
  <div class="info-block" style="margin-top:40px">
    <h3>Kelowna</h3>
    <ul><li>https://www.lakesidebusiness.ca/</li><li>https://www.visitlakeside.ca/</li><li>https://lakesidevalleyguide.ca/</li><li>https://www.lakesidecityhall.ca/</li><li>https://www.lakesideregionhub.ca/</li><li>https://www.lakesidevalleyinfo.ca/index.html</li></ul>
  </div>
</section>

</body>
</html>
```